Harborline Energy - needs a business card

Harborline Energy is a U.S. based diesel sourcing and distribution company that supports American oil & gas fields through providing quality product and consistent services.

Target Market(s)

Oil and Gas

Contact Information for Business Card

The background of the card must be white to ensure the logo pops.

Font styles to use
Serif
Sans Serif

Colors

Designer to choose colors to be used in the design.

Requirements
Must have
• Front of Card: Tag line: Harborline Energy, Powering America's Oil & Gas fields.
• Not sure if you guys do this part but just in case...
• Dale Menschow
• Owner/CEO
• C:555.318.4076
• E:Dmenschow@harborlineenergy.example
• W:Harborlineenergy.example
• Locations: Servicing the Powder River, DJ basin and Bakken formations.
• Back of Card: " Frac fueling is what we do. We understand how important diesel fuel is to your operation, which is why our main service line is Frac fueling. We assure our supply and stand by our service"

```html
<!DOCTYPE html>
<html lang="en">
<head>
<meta charset="utf-8">
<title>Harborline Energy – Business Card</title>
<link rel="stylesheet" href="https://fonts.googleapis.com/css2?family=Roboto:wght@400;500;700&display=swap">
<style>
  :root{
    --navy:#1b2d5c;
    --red:#b3161d;
    --white:#ffffff;
    --ink:#1d1d1f;
    --stage:#9aa8b0;
  }
  html,body{margin:0;padding:0;overflow:hidden;}
  body{
    width:1200px;height:900px;
    background:var(--stage);
    font-family:"Roboto",Arial,sans-serif;
    position:relative;
  }
  .card{
    position:absolute;
    width:630px;height:360px;
    border-radius:22px;
    box-shadow:0 10px 24px rgba(0,0,0,.25);
    overflow:hidden;
  }
  /* back of card */
  .card--back{left:110px;top:50px;background:var(--navy);color:var(--white);text-align:center;}
  .brand{display:inline-flex;align-items:center;gap:12px;font-weight:700;letter-spacing:.04em;text-transform:uppercase;white-space:nowrap;}
  .brand__dot{width:18px;height:18px;border-radius:50%;flex:none;}
  .card--back .brand{margin-top:96px;font-size:34px;}
  .card--back .brand__dot{background:var(--white);}
  .quote{margin:58px 60px 0;font-size:15px;line-height:1.4;}
  .web{margin-top:10px;font-size:15px;}
  /* front of card */
  .card--front{left:460px;top:500px;background:var(--white);color:var(--ink);}
  .card--front .brand{position:absolute;left:40px;top:104px;font-size:27px;color:var(--navy);}
  .card--front .brand__dot{background:var(--red);}
  .person{position:absolute;right:60px;top:140px;text-align:right;}
  .person__name{font-size:24px;font-weight:700;color:var(--navy);letter-spacing:-.01em;}
  .person__role{font-size:11px;font-weight:500;margin-top:2px;}
  .rule{position:absolute;left:40px;right:60px;top:198px;height:3px;background:var(--red);}
  .locations{position:absolute;right:60px;top:212px;margin:0;text-align:right;font-size:14px;line-height:1.35;}
  .contacts{position:absolute;left:40px;top:258px;list-style:none;margin:0;padding:0;}
  .contacts li{display:flex;align-items:center;gap:14px;font-size:15px;height:29px;white-space:nowrap;}
  .icon{width:22px;height:22px;background:var(--navy);display:flex;align-items:center;justify-content:center;flex:none;}
</style>
</head>
<body>

<section class="card card--back">
  <div class="brand"><span class="brand__dot"></span>Harborline Energy</div>
  <p class="quote">" Frac fueling is what we do. We understand how important diesel fuel is to your operation, which is why our main service line is Frac fueling. We assure our supply and stand by our service"</p>
  <div class="web">www.Harborlineenergy.example</div>
</section>

<section class="card card--front">
  <div class="brand"><span class="brand__dot"></span>Harborline Energy</div>
  <div class="person">
    <div class="person__name">Dale Menschow</div>
    <div class="person__role">Owner/CEO</div>
  </div>
  <div class="rule"></div>
  <p class="locations">Servicing the Powder River,<br>DJ basin and Bakken formations.</p>
  <ul class="contacts">
    <li><span class="icon"><svg width="14" height="14" viewBox="0 0 24 24"><path fill="#fff" d="M6.6 10.8a15 15 0 0 0 6.6 6.6l2.2-2.2a1 1 0 0 1 1-.25 11.4 11.4 0 0 0 3.6.57 1 1 0 0 1 1 1V20a1 1 0 0 1-1 1A17 17 0 0 1 3 4a1 1 0 0 1 1-1h3.5a1 1 0 0 1 1 1c0 1.25.2 2.450.57 3.57a1 1 0 0 1-.25 1z"/></svg></span>555.318.4076</li>
    <li><span class="icon"><svg width="14" height="14" viewBox="0 0 24 24"><rect x="3" y="6" width="18" height="12" fill="none" stroke="#fff" stroke-width="2"/><path d="M3 6l9 7 9-7" fill="none" stroke="#fff" stroke-width="2"/></svg></span>Dmenschow@harborlineenergy.example</li>
    <li><span class="icon"><svg width="14" height="14" viewBox="0 0 24 24"><circle cx="12" cy="12" r="9" fill="none" stroke="#fff" stroke-width="2"/><path d="M3 12h18M12 3c3 3 3 15 0 18M12 3c-3 3-3 15 0 18" fill="none" stroke="#fff" stroke-width="1.6"/></svg></span>Harborlineenergy.example</li>
  </ul>
</section>

</body>
</html>
```